Flyer-Design für Software für Gebäudedienstleister
Zielgruppe
Software für Gebäudedienstleister,
Softwarevertrieb, Durchführung von Schulungen,
Aufgabenstellung
Erstellt werden soll eine Din A4 Seite mit Wickelfalz (6Seiten)
Für den Neustart einer Software für Gebäudedienstleister möchten wir einen modernen
Flyer mit ansprechendem Text anfertigen lassen.
Die Software funktioniert Online oder Lokal.
Ein Tablet-Service wird angeboten.
Eine elektronische Planungstafel bietet die Software.
Terminplanung mittels "Drag & Drop" möglich
1-Klick Funktion in der Rückmeldung von Arbeitsscheinen und in der anschließenden Fakturierung.
Durchführung von Schulungen Akademie
Texte:
1.Fakturierung
Mit Vantoruk® Faktura liefern wir Ihnen ein leicht zu bedienendes Modul
Die Vantoruk®Fakturierungssoftware zeichnet sich durch einfache Handhabung aus:
Moderne Faktura Software
Leicht zu bedienen
Gut strukturierte Benutzeroberfläche
Praxisorientierte Funktionen
Sofort einsatzbereit
1-Klick Fakturierung
Mit Vantoruk® fakturieren Sie schnell und effektiv.
2. Personaleinsatzplanung Drag & Drop
Die Einsatzplanung erfolgt in Vantoruk® mit nur wenigen Schritten.
Dabei berücksichtigt das System z.B. die Regionen, in denen Sie
tätig sind und verhindert somit unnötige Fahrzeiten.
Pausen werden automatisch erfasst. Touren planen Sie bereits
bequem per Drag & Drop auf dem Gesamtkalender.
3. Planungstafel
Mit Vantoruk® planen Sie einfach und schnell Termine.
Mit unserer elektronischen Planungstafel behalten Sie immer
einen optimalen Überblick über Ihre Ressourcen.
Vantoruk® ist die intelligente Lösung für Ihre Personaleinsatzplanung.
4. Tabletservice
Bieten Sie Ihrem Kunden mit Vantoruk® einen echten Mehrwert
Sie möchten Ihrem Kunden gegenüber als modernes und zielorientiertes
Unternehmen auftreten?
Setzen Sie ab jetzt unseren Tablet-Service in Ihrem Betrieb ein.
Egal ob Arbeitsschein zurückmelden, schnell ein Foto vom Wintergarten,
oder eine Unterschrift fü..

```html
<!DOCTYPE html>
<html lang="de">
<head>
<meta charset="utf-8">
<title>Vantoruk – Wickelfalz-Flyer</title>
<link rel="stylesheet" href="https://fonts.googleapis.com/css2?family=Quicksand:wght@400;500&family=Questrial&display=swap">
<style>
  :root {
    --green: #adb935;
    --slate: #5d6073;
    --ink: #5a5c68;
    --paper: #ffffff;
    --label: #111111;
    --bar-blue: #9cc3e5;
    --bar-olive: #c9c79a;
    --mark-pink: #f2d3d7;
  }
  html, body { margin: 0; padding: 0; overflow: hidden; background: var(--paper); }
  .canvas { width: 1200px; height: 1200px; display: block; }
  .headline { font-family: "Quicksand", sans-serif; font-weight: 400; font-size: 34px; }
  .headline--slate { fill: var(--slate); }
  .headline--green { fill: var(--green); }
  .body-copy { font-family: "Quicksand", sans-serif; font-size: 10.5px; fill: var(--ink); }
  .feature-list { font-family: "Quicksand", sans-serif; font-size: 14.5px; fill: var(--ink); }
  .cover-title { font-family: "Quicksand", sans-serif; font-weight: 400; fill: var(--paper); }
  .brand-name { font-family: "Quicksand", sans-serif; font-weight: 500; font-size: 36px; fill: var(--paper); }
  .contact { font-family: "Quicksand", sans-serif; font-size: 11px; fill: var(--paper); }
  .panel-label { font-family: "Questrial", sans-serif; font-size: 40px; fill: var(--label); letter-spacing: 1px; }
  .planner-text { font-family: "Quicksand", sans-serif; font-size: 4.5px; fill: #555; }
  .planner-title { font-family: "Quicksand", sans-serif; font-size: 6px; font-weight: 500; fill: #333; }
</style>
</head>
<body>
<svg class="canvas" viewBox="0 0 1920 1920" xmlns="http://www.w3.org/2000/svg">
  <defs>
    <filter id="panel-shadow" x="-5%" y="-5%" width="110%" height="110%">
      <feDropShadow dx="0" dy="4" stdDeviation="4" flood-color="#000" flood-opacity="0.35"/>
    </filter>
    <linearGradient id="tone-building" x1="0" y1="0" x2="1" y2="1">
      <stop offset="0" stop-color="#c9d0d8"/><stop offset="0.6" stop-color="#9aa8b8"/><stop offset="1" stop-color="#7b96c8"/>
    </linearGradient>
    <linearGradient id="tone-desk" x1="0" y1="0" x2="0" y2="1">
      <stop offset="0" stop-color="#f4f5f6"/><stop offset="1" stop-color="#dcdfe3"/>
    </linearGradient>
    <linearGradient id="tone-notes" x1="0" y1="0" x2="1" y2="0">
      <stop offset="0" stop-color="#b7d03f"/><stop offset="0.5" stop-color="#8e9a62"/><stop offset="1" stop-color="#b7d03f"/>
    </linearGradient>
    <linearGradient id="tone-office" x1="0" y1="0" x2="0" y2="1">
      <stop offset="0" stop-color="#aab6c6"/><stop offset="0.55" stop-color="#6b5446"/><stop offset="1" stop-color="#5d7a45"/>
    </linearGradient>
    <linearGradient id="tone-tablet" x1="0" y1="0" x2="1" y2="1">
      <stop offset="0" stop-color="#8fa43a"/><stop offset="1" stop-color="#b5d14e"/>
    </linearGradient>
    <clipPath id="cover-clip"><rect x="0" y="0" width="316" height="670"/></clipPath>

    <!-- Title panel, drawn in local coordinates -->
    <g id="cover-panel">
      <g clip-path="url(#cover-clip)">
        <rect x="0" y="0" width="316" height="670" fill="var(--paper)"/>
        <polygon role="img" aria-label="Foto: moderne geschwungene Bürofassade mit Hochhäusern" points="14,0 316,0 316,280 267,292" fill="url(#tone-building)"/>
        <polygon points="0,30 267,297 0,563" fill="var(--green)"/>
        <polyline points="-18,30 268,281 12,563" fill="none" stroke="var(--slate)" stroke-width="1"/>
        <polygon points="15,578 284,311 316,343 316,670 105,670" fill="var(--slate)"/>
        <text class="cover-title" x="9" y="215" font-size="50">DIE</text>
        <text class="cover-title" x="13" y="263" font-size="38">Software</text>
        <text class="cover-title" x="13" y="303" font-size="28">für</text>
        <text class="cover-title" x="13" y="341" font-size="34">Gebäude-</text>
        <text class="cover-title" x="13" y="373" font-size="34">dienstleister</text>
        <circle cx="72" cy="583" r="9" fill="var(--green)"/>
        <text class="brand-name" x="88" y="596">Vantoruk</text>
      </g>
    </g>

    <!-- Scheduling board table -->
    <g id="planner">
      <text class="planner-title" x="0" y="0">Terminplaner</text>
      <g fill="var(--green)">
        <rect x="10" y="8" width="34" height="7"/><rect x="48" y="8" width="32" height="7"/>
        <rect x="84" y="8" width="16" height="7"/><rect x="104" y="8" width="10" height="7"/>
        <rect x="117" y="8" width="14" height="7"/><rect x="134" y="8" width="14" height="7"/>
        <rect x="151" y="8" width="10" height="7"/><rect x="212" y="8" width="12" height="7"/>
        <rect x="228" y="8" width="14" height="7"/><rect x="246" y="8" width="14" height="7"/>
        <rect x="264" y="8" width="14" height="7"/>
      </g>
      <text class="planner-text" x="166" y="14">Fr 14.04.</text>
      <rect x="0" y="20" width="289" height="74" fill="#fff" stroke="#c8c8c8" stroke-width="0.6"/>
      <text class="planner-text" x="70" y="26">Do 13.04.</text>
      <text class="planner-text" x="190" y="26">Fr 14.04.</text>
      <rect x="106" y="30" width="6" height="64" fill="var(--mark-pink)"/>
      <rect x="182" y="30" width="6" height="64" fill="var(--mark-pink)"/>
      <g stroke="#dcdcdc" stroke-width="0.5">
        <line x1="0" y1="30" x2="289" y2="30"/><line x1="0" y1="38" x2="289" y2="38"/>
        <line x1="0" y1="47" x2="289" y2="47"/><line x1="0" y1="56" x2="289" y2="56"/>
        <line x1="0" y1="65" x2="289" y2="65"/><line x1="0" y1="74" x2="289" y2="74"/>
        <line x1="0" y1="83" x2="289" y2="83"/>
        <line x1="58" y1="20" x2="58" y2="94"/><line x1="70" y1="30" x2="70" y2="94"/>
        <line x1="82" y1="30" x2="82" y2="94"/><line x1="94" y1="30" x2="94" y2="94"/>
        <line x1="106" y1="30" x2="106" y2="94"/><line x1="118" y1="30" x2="118" y2="94"/>
        <line x1="130" y1="30" x2="130" y2="94"/><line x1="142" y1="30" x2="142" y2="94"/>
        <line x1="154" y1="30" x2="154" y2="94"/><line x1="166" y1="30" x2="166" y2="94"/>
        <line x1="178" y1="30" x2="178" y2="94"/><line x1="190" y1="30" x2="190" y2="94"/>
        <line x1="202" y1="30" x2="202" y2="94"/><line x1="214" y1="30" x2="214" y2="94"/>
        <line x1="226" y1="30" x2="226" y2="94"/><line x1="238" y1="30" x2="238" y2="94"/>
        <line x1="250" y1="30" x2="250" y2="94"/><line x1="262" y1="30" x2="262" y2="94"/>
        <line x1="274" y1="30" x2="274" y2="94"/>
      </g>
      <text class="planner-text" x="3" y="44">Meyer</text>
      <text class="planner-text" x="3" y="53">Berger</text>
      <text class="planner-text" x="3" y="62">Santos</text>
      <text class="planner-text" x="3" y="71">Müller</text>
      <text class="planner-text" x="3" y="80">Braun</text>
      <rect x="264" y="39" width="24" height="6" fill="var(--bar-blue)"/>
      <rect x="84" y="48" width="24" height="6" fill="var(--bar-olive)"/>
      <rect x="236" y="48" width="52" height="6" fill="var(--bar-olive)"/>
      <rect x="112" y="57" width="26" height="6" fill="#d6e7f4"/>
      <rect x="190" y="57" width="26" height="6" fill="#d6e7f4"/>
      <rect x="84" y="66" width="140" height="6" fill="var(--bar-blue)"/>
      <rect x="252" y="75" width="26" height="6" fill="#d6e7f4"/>
    </g>
  </defs>

  <!-- ===== Outside spread ===== -->
  <g class="spread spread--outside" filter="url(#panel-shadow)">
    <rect x="299" y="140" width="948" height="670" fill="var(--paper)"/>
  </g>
  <g class="spread-content">
    <!-- Invoicing page -->
    <polyline points="312,140 312,203 585,203" fill="none" stroke="var(--green)" stroke-width="1.5"/>
    <polygon points="543,140 615,140 615,235" fill="var(--slate)"/>
    <text class="headline headline--slate" x="337" y="192">Fakturierung</text>
    <text class="body-copy">
      <tspan x="324" y="252">Lorem ipsum dolor sit amet, consectetuer adipiscing</tspan>
      <tspan x="324" y="264">elit. Aenean commodo ligula eget dolor. Aenean</tspan>
      <tspan x="324" y="275">massa. Cum sociis natoque penatibus et magnis dis</tspan>
      <tspan x="324" y="287">parturient montes, nascetur ridiculus mus. Donec quam</tspan>
      <tspan x="324" y="298">felis, ultricies nec, pellentesque eu, pretium quis, sem.</tspan>
      <tspan x="324" y="310">Nulla consequat massa quis enim. Donec pede justo,</tspan>
      <tspan x="324" y="321">fringilla vel, aliquet nec, vulputate eget, arcu.</tspan>
    </text>
    <g fill="var(--green)">
      <circle cx="327" cy="346" r="1.6"/><circle cx="327" cy="358" r="1.6"/><circle cx="327" cy="369" r="1.6"/>
      <circle cx="327" cy="381" r="1.6"/><circle cx="327" cy="392" r="1.6"/><circle cx="327" cy="404" r="1.6"/>
    </g>
    <text class="body-copy">
      <tspan x="333" y="350">Lorem ipsum</tspan><tspan x="333" y="362">Lorem ipsum</tspan>
      <tspan x="333" y="373">Lorem ipsum</tspan><tspan x="333" y="385">Lorem ipsum</tspan>
      <tspan x="333" y="396">Lorem ipsum</tspan><tspan x="333" y="408">Lorem ipsum</tspan>
    </text>
    <text class="body-copy">
      <tspan x="324" y="449">Lorem ipsum dolor sit amet, consectetuer adipiscing</tspan>
      <tspan x="324" y="461">elit. Aenean commodo ligula eget dolor. Aenean</tspan>
      <tspan x="324" y="472">massa. Cum sociis natoque penatibus et magnis dis</tspan>
      <tspan x="324" y="484">parturient montes, nascetur ridiculus mus. Donec quam</tspan>
      <tspan x="324" y="495">felis, ultricies nec, pellentesque eu, pretium quis, sem.</tspan>
    </text>
    <rect role="img" aria-label="Foto: Schreibtisch mit Laptop und Monitor mit Balkendiagramm" x="299" y="560" width="316" height="250" fill="url(#tone-desk)"/>

    <!-- Back page on outside -->
    <polygon points="615,485 651,451 918,718 826,810 615,810" fill="var(--slate)"/>
    <polygon points="664,437 931,170 931,703" fill="var(--green)"/>
    <polyline points="913,170 664,449 943,703" fill="none" stroke="var(--slate)" stroke-width="1"/>
    <text class="contact">
      <tspan x="651" y="683">Adresse</tspan><tspan x="651" y="696">Strasse</tspan>
      <tspan x="651" y="709">PLZ, Ort</tspan><tspan x="651" y="721">Tel</tspan>
      <tspan x="651" y="734">Mail</tspan><tspan x="651" y="747">www</tspan>
    </text>

    <use href="#cover-panel" x="931" y="140"/>
  </g>
  <text class="panel-label" x="342" y="870">aussen</text>

  <!-- ===== Title panel ===== -->
  <g filter="url(#panel-shadow)"><rect x="1317" y="140" width="313" height="670" fill="var(--paper)"/></g>
  <svg x="1317" y="140" width="313" height="670" viewBox="0 0 313 670" overflow="hidden">
    <use href="#cover-panel"/>
  </svg>
  <text class="panel-label" x="1417" y="878">Titel</text>

  <!-- ===== Inside spread ===== -->
  <g filter="url(#panel-shadow)"><rect x="299" y="940" width="948" height="670" fill="var(--paper)"/></g>
  <g class="spread-content">
    <!-- Planning board -->
    <polygon points="299,940 317,940 348,971 299,1004" fill="var(--green)"/>
    <polyline points="330,1003 602,1003 602,940" fill="none" stroke="var(--slate)" stroke-width="1.2"/>
    <text class="headline headline--green" x="380" y="983">Planungstafel</text>
    <text class="body-copy">
      <tspan x="321" y="1046">Lorem ipsum dolor sit amet, consectetuer adipiscing elit.</tspan>
      <tspan x="321" y="1058">Aenean commodo ligula eget dolor. Aenean massa. Cum</tspan>
      <tspan x="321" y="1069">sociis natoque penatibus et magnis dis parturient montes,</tspan>
      <tspan x="321" y="1081">nascetur ridiculus mus. Donec quam felis, ultricies nec,</tspan>
      <tspan x="321" y="1092">pellentesque eu, pretium quis, sem. Nulla consequat mas-</tspan>
      <tspan x="321" y="1104">sa quis enim. Donec pede justo, fringilla vel, aliquet nec,</tspan>
      <tspan x="321" y="1115">vulputate eget, arcu.</tspan>
    </text>
    <use href="#planner" x="313" y="1155"/>

    <!-- Drag & Drop -->
    <polygon points="541,1317 615,1245 615,1390" fill="var(--slate)"/>
    <polyline points="560,1319 312,1319 312,1382 607,1382" fill="none" stroke="var(--green)" stroke-width="1.5"/>
    <text class="headline headline--slate" x="318" y="1363">Drag &amp; Drop</text>
    <text class="body-copy">
      <tspan x="324" y="1427">Lorem ipsum dolor sit amet, consectetuer adipiscing</tspan>
      <tspan x="324" y="1439">elit. Aenean commodo ligula eget dolor. Aenean</tspan>
      <tspan x="324" y="1450">massa. Cum sociis natoque penatibus et magnis dis</tspan>
      <tspan x="324" y="1462">parturient montes, nascetur ridiculus mus. Donec quam</tspan>
      <tspan x="324" y="1473">felis, ultricies nec, pellentesque eu, pretium quis, sem.</tspan>
      <tspan x="324" y="1485">Nulla consequat massa quis enim. Donec pede justo,</tspan>
      <tspan x="324" y="1496">fringilla vel, aliquet nec, vulputate eget, arcu.</tspan>
    </text>
    <svg x="299" y="1520" width="316" height="90" overflow="hidden">
      <use href="#planner" x="14" y="6"/>
    </svg>

    <!-- Middle: feature overview -->
    <rect role="img" aria-label="Foto: Mann hinter einer Glaswand mit grünen Haftnotizen" x="628" y="940" width="303" height="165" fill="url(#tone-notes)"/>
    <g fill="none" stroke-width="1">
      <polyline points="615,1230 715,1123 931,1305" stroke="var(--slate)"/>
      <polyline points="615,1245 737,1123 931,1290" stroke="var(--green)"/>
      <line x1="615" y1="1533" x2="705" y2="1610" stroke="var(--slate)"/>
      <line x1="615" y1="1545" x2="690" y2="1610" stroke="var(--green)"/>
      <line x1="931" y1="1465" x2="800" y2="1610" stroke="var(--slate)"/>
      <line x1="931" y1="1455" x2="785" y2="1610" stroke="var(--green)"/>
    </g>
    <g fill="var(--green)">
      <polygon points="670,1259 675,1264 670,1269 665,1264"/><polygon points="670,1291 675,1296 670,1301 665,1296"/>
      <polygon points="670,1324 675,1329 670,1334 665,1329"/><polygon points="670,1356 675,1361 670,1366 665,1361"/>
      <polygon points="670,1389 675,1394 670,1399 665,1394"/><polygon points="670,1421 675,1426 670,1431 665,1426"/>
      <polygon points="670,1454 675,1459 670,1464 665,1459"/><polygon points="670,1486 675,1491 670,1496 665,1491"/>
    </g>
    <text class="feature-list">
      <tspan x="690" y="1269">Online oder Lokal</tspan>
      <tspan x="690" y="1301">Personaleinsatzplanung</tspan>
      <tspan x="690" y="1334">Kunden, Objekte, Auftrag</tspan>
      <tspan x="690" y="1366">Fakturierung</tspan>
      <tspan x="690" y="1399">Artikelverkauf</tspan>
      <tspan x="690" y="1431">Wartungsplaner</tspan>
      <tspan x="690" y="1464">Datenschnittstellen</tspan>
      <tspan x="690" y="1496">Akademie, Schulungen</tspan>
    </text>

    <!-- Academy -->
    <polyline points="944,940 944,1003 1200,1003" fill="none" stroke="var(--green)" stroke-width="1.5"/>
    <polygon points="1163,940 1247,940 1247,1045" fill="var(--slate)"/>
    <text class="headline headline--slate" x="957" y="982">Akademie</text>
    <text class="body-copy">
      <tspan x="944" y="1046">Lorem ipsum dolor sit amet, consectetuer adipiscing elit.</tspan>
      <tspan x="944" y="1058">Aenean commodo ligula eget dolor. Aenean massa. Cum</tspan>
      <tspan x="944" y="1069">sociis natoque penatibus et magnis dis parturient montes,</tspan>
      <tspan x="944" y="1081">nascetur ridiculus mus. Donec quam felis, ultricies nec,</tspan>
    </text>
    <g fill="var(--slate)">
      <polygon points="984,1112 988,1116 984,1120 980,1116"/><polygon points="984,1130 988,1134 984,1138 980,1134"/>
      <polygon points="984,1148 988,1152 984,1156 980,1152"/><polygon points="984,1166 988,1170 984,1174 980,1170"/>
    </g>
    <text class="body-copy">
      <tspan x="992" y="1120">Schulung 1</tspan><tspan x="992" y="1138">Schulung 2</tspan>
      <tspan x="992" y="1156">Schulung 3</tspan><tspan x="992" y="1174">Schulung 4</tspan>
    </text>
    <rect role="img" aria-label="Foto: moderner Bürokomplex mit Glasfassade" x="944" y="1210" width="291" height="113" fill="url(#tone-office)"/>

    <!-- Tablet service -->
    <polygon points="931,1318 1005,1390 931,1465" fill="var(--green)"/>
    <polyline points="1003,1377 1235,1377 1235,1453 944,1453" fill="none" stroke="var(--slate)" stroke-width="1.2"/>
    <text class="headline headline--green" x="1003" y="1425">Tabletservice</text>
    <text class="body-copy">
      <tspan x="944" y="1506">Lorem ipsum dolor sit amet,</tspan>
      <tspan x="944" y="1518">consectetuer adipiscing elit.</tspan>
      <tspan x="944" y="1529">Aenean commodo ligula eget</tspan>
      <tspan x="944" y="1541">dolor. Aenean massa. Cum</tspan>
      <tspan x="944" y="1552">sociis natoque penatibus et</tspan>
      <tspan x="944" y="1564">magnis dis parturient montes,</tspan>
      <tspan x="944" y="1575">nascetur ridiculus mus.</tspan>
    </text>
    <rect role="img" aria-label="Illustration: Tablet mit Arbeitsschein" x="1112" y="1499" width="123" height="79" fill="url(#tone-tablet)"/>
  </g>
  <text class="panel-label" x="342" y="1686">innen</text>

  <!-- ===== Back panel ===== -->
  <g filter="url(#panel-shadow)"><rect x="1318" y="940" width="315" height="670" fill="var(--paper)"/></g>
  <g class="spread-content">
    <polygon points="1365,1240 1633,972 1633,1502" fill="var(--green)"/>
    <polyline points="1615,968 1368,1252 1633,1490" fill="none" stroke="var(--slate)" stroke-width="1"/>
    <polygon points="1318,1280 1350,1249 1620,1518 1530,1610 1318,1610" fill="var(--slate)"/>
    <text class="contact">
      <tspan x="1352" y="1483">Adresse</tspan><tspan x="1352" y="1496">Strasse</tspan>
      <tspan x="1352" y="1509">PLZ, Ort</tspan><tspan x="1352" y="1521">Tel</tspan>
      <tspan x="1352" y="1534">Mail</tspan><tspan x="1352" y="1547">www</tspan>
    </text>
  </g>
  <text class="panel-label" x="1397" y="1681">Rückseite</text>
</svg>
</body>
</html>
```